Marbrook Chiropractic Center, PLLC sign

I need a design for a sign that will hang from a light post by the road and lets people know that my business is inside the big medical building nearby. I would like it to catch the eye of passing motorists. The design should fit on a sign that is 3 feet wide and 5 feet long. I am a Chiropractor and treat a wide range of patients. I would like the sign to look professional, but eyecatching.

The provided business logo is a .jpg. I can provide .eps if that would be better.
I like the colors in my Marbrook Chiropractic logo.

Marbrook Chiropractic Center, PLLC
(555) 287-4163
www.marbrookspine-example.com
If space allows, please include (listed from most important to least important to include):
• Short Term Care For Your Neck & Back Pain
• No Referral Needed
• Affordable / Insurance Accepted
• Proficient in treating Soft Tissue Problems

Industry/Entity Type

Medical

Requirements
Must have
• logos
website
phone number
Nice to have
• the bullet points
Should not have
• a spine

```html
<!DOCTYPE html>
<html lang="en">
<head>
<meta charset="utf-8">
<title>Marbrook Chiropractic Sign</title>
<link href="https://fonts.googleapis.com/css2?family=Cinzel:wght@600&family=Tenor+Sans&family=Arimo:wght@700&display=swap" rel="stylesheet">
<style>
  :root {
    --frame: #000000;
    --paper: #ffffff;
    --ink: #111111;
    --rule: #b9b9b9;
    --band: #dcdbdb;
    --accent: #1fa8e0;
    --mark: #2f2f9c;
    --badge-red: #d8232a;
    --badge-blue: #1d4fa0;
    --arrow-light: #f4f4f4;
    --arrow-dark: #b4b4b4;
  }
  * { margin: 0; padding: 0; box-sizing: border-box; }
  html, body { width: 1200px; height: 900px; overflow: hidden; background: var(--frame); }
  .sign {
    position: relative; width: 1200px; height: 900px; background: var(--frame);
  }
  .sign-face {
    position: absolute; left: 0; top: 88px; width: 1200px; height: 722px;
    background: var(--paper);
  }
  .direction-arrow { position: absolute; left: 676px; top: 30px; }
  .brand-word {
    position: absolute; top: 187px;
    font-family: "Tenor Sans", sans-serif; color: var(--ink);
    text-transform: uppercase; font-size: 62px; letter-spacing: 0; line-height: 1;
    white-space: nowrap;
  }
  .brand-word .initial { font-size: 88px; }
  .brand-word--first { left: 40px; }
  .brand-word--second { left: 552px; }
  .brand-rule { position: absolute; top: 285px; height: 1px; background: var(--rule); }
  .brand-rule--first { left: 40px; width: 406px; }
  .brand-rule--second { left: 560px; width: 566px; }
  .brand-dot {
    position: absolute; left: 472px; top: 200px; width: 60px; height: 60px;
    border-radius: 50%; background: var(--mark);
  }
  .partner-badge--oval {
    position: absolute; left: 35px; top: 408px; width: 215px; height: 58px;
    border-radius: 50%; background: var(--badge-red);
  }
  .partner-divider {
    position: absolute; left: 282px; top: 406px; width: 1px; height: 62px; background: var(--rule);
  }
  .partner-badge--bar {
    position: absolute; left: 316px; top: 414px; width: 186px; height: 46px; background: var(--badge-blue);
  }
  .benefits {
    position: absolute; left: 636px; top: 419px; list-style: none;
    font-family: "Arimo", Arial, sans-serif; font-weight: 700; font-size: 24px;
    color: var(--accent); line-height: 29px; white-space: nowrap;
  }
  .benefits li::before { content: "\2022"; margin-right: 8px; }
  .contact-band {
    position: absolute; left: 0; top: 575px; width: 1200px; height: 147px;
    background: var(--band); padding-top: 14px;
    font-family: "Cinzel", serif; font-weight: 600; color: var(--ink);
    font-size: 28px; line-height: 38px; text-align: center; letter-spacing: 1px;
    white-space: nowrap;
  }
</style>
</head>
<body>
<main class="sign">
  <section class="sign-face">
    <svg class="direction-arrow" width="452" height="150" viewBox="0 0 452 150" aria-hidden="true">
      <defs>
        <linearGradient id="arrowFade" x1="0" x2="1" y1="0" y2="0">
          <stop offset="0" stop-color="var(--arrow-light)" stop-opacity="0"/>
          <stop offset="0.55" stop-color="#cfcfcf"/>
          <stop offset="1" stop-color="var(--arrow-dark)"/>
        </linearGradient>
      </defs>
      <polygon points="0,60 330,60 310,2 450,75 310,146 330,90 0,90" fill="url(#arrowFade)"/>
    </svg>

    <div class="brand-word brand-word--first"><span class="initial">M</span>arbrook</div>
    <div class="brand-rule brand-rule--first"></div>
    <div class="brand-dot" aria-hidden="true"></div>
    <div class="brand-word brand-word--second"><span class="initial">C</span>hiropractic</div>
    <div class="brand-rule brand-rule--second"></div>

    <div class="partner-badge--oval" role="img" aria-label="Partner certification badge"></div>
    <div class="partner-divider"></div>
    <div class="partner-badge--bar" role="img" aria-label="Proud partner badge"></div>

    <ul class="benefits">
      <li>Short Term Care For Your Neck &amp; Back Pain</li>
      <li>No Referral Needed</li>
      <li>Affordable / Insurance Accepted</li>
      <li>Proficient in treating Soft Tissue Problems</li>
    </ul>

    <footer class="contact-band">
      <p>Find us : 418 Harbor Crest Avenue, Suite H, Lakeview, NC 27999</p>
      <p>Make an Appointment : info@marbrookspine-example.com</p>
      <p>Tel: 555-287-4163 Fax: 555-287-4170</p>
    </footer>
  </section>
</main>
</body>
</html>
```